Business Card Project

Hello,

Please find attached files for use for our business card design.

We have attached all the version of the trades licensing council to the project for insertion onto our business card.

Details to be on the card are:
We are a construction management company. Please ensure that there is space to add our personal contact details. We would like the cards to be double sided with our logo on one side and our details on the other

Thanks,

Marcel

Good Evening,

Please ensure with all design submissions, that the 'certified works overseer' logo is on the card designs.

Thanks,

Marcel

Industry/Entity Type

Construction

```html
<!DOCTYPE html>
<html lang="en">
<head>
<meta charset="utf-8">
<title>Halden Group – Business Card</title>
<link rel="stylesheet" href="https://fonts.googleapis.com/css2?family=Arimo:ital,wght@0,400;0,700;1,400&family=Marcellus+SC&display=swap">
<style>
  :root {
    --canvas: #e4e3e6;
    --card: #ffffff;
    --panel: #5e5f61;
    --brand-brown: #4a2616;
    --ink: #2b1a12;
    --muted: #6d6d6d;
    --rule: #c9c9c9;
    --panel-text: #f1f1f1;
  }
  * { box-sizing: border-box; margin: 0; padding: 0; }
  html, body {
    width: 1200px; height: 900px; overflow: hidden;
    background: var(--canvas);
    font-family: "Arimo", Arial, sans-serif;
  }
  .stage {
    position: relative; width: 1200px; height: 900px;
  }
  .card {
    position: absolute; top: 295px;
    width: 540px; height: 310px;
    background: var(--card);
    box-shadow: 0 3px 10px rgba(0,0,0,0.28);
    overflow: hidden;
  }
  .card--front { left: 45px; }
  .card--back { left: 615px; }

  /* Front */
  .brand {
    position: absolute; left: 0; right: 0; top: 120px;
    display: flex; align-items: center; justify-content: center; gap: 14px;
  }
  .brand__mark {
    width: 30px; height: 30px; background: var(--brand-brown);
  }
  .brand__name {
    font-weight: 700; font-size: 54px; letter-spacing: -1px;
    color: var(--brand-brown); line-height: 1;
  }
  .brand__rule {
    position: absolute; top: 150px; width: 80px; height: 2px;
    background: linear-gradient(90deg, transparent, var(--rule), transparent);
  }
  .brand__rule--left { left: 45px; }
  .brand__rule--right { right: 45px; }
  .brand__sub {
    position: absolute; top: 188px; left: 0; right: 0;
    text-align: center; font-size: 9px; color: var(--muted); letter-spacing: 0.5px;
  }

  /* Back */
  .identity {
    position: absolute; left: 0; top: 0; width: 278px; height: 100%;
  }
  .identity__name {
    position: absolute; top: 122px; left: 0; right: 0; text-align: center;
    font-family: "Marcellus SC", Georgia, serif; font-size: 21px; color: var(--ink);
    letter-spacing: 0.5px;
  }
  .identity__role {
    position: absolute; top: 152px; left: 0; right: 0; text-align: center;
    font-style: italic; font-size: 12px; color: var(--ink);
  }
  .accreditation {
    position: absolute; left: 14px; bottom: 16px;
    display: flex; align-items: center; gap: 6px;
  }
  .accreditation__seal {
    width: 30px; height: 30px; border-radius: 50%;
    border: 2px solid #8a8a8a; background: #f4f4f4;
  }
  .accreditation__text {
    font-size: 13px; font-weight: 700; color: #333; line-height: 1;
  }
  .accreditation__text small {
    display: block; font-size: 8px; font-weight: 400; margin-top: 1px;
  }
  .contact {
    position: absolute; right: 0; top: 0; width: 262px; height: 100%;
    background: var(--panel);
    padding: 92px 0 0 42px;
    list-style: none; color: var(--panel-text); font-size: 11px;
  }
  .contact__item {
    display: flex; align-items: flex-start; gap: 12px; margin-bottom: 9px; line-height: 1.25;
  }
  .contact__icon { width: 14px; height: 14px; flex: none; fill: var(--panel-text); }
</style>
</head>
<body>
<main class="stage">
  <section class="card card--front" aria-label="Card front">
    <span class="brand__rule brand__rule--left"></span>
    <div class="brand">
      <span class="brand__mark"></span>
      <span class="brand__name">HALDEN</span>
    </div>
    <span class="brand__rule brand__rule--right"></span>
    <p class="brand__sub">Group</p>
  </section>

  <section class="card card--back" aria-label="Card back">
    <div class="identity">
      <h1 class="identity__name">Name Surname</h1>
      <p class="identity__role">profession</p>
      <div class="accreditation">
        <span class="accreditation__seal"></span>
        <p class="accreditation__text">CERTIFIED<small>Works Overseer</small></p>
      </div>
    </div>
    <ul class="contact">
      <li class="contact__item">
        <svg class="contact__icon" viewBox="0 0 16 16"><path d="M8 1 1 8h2v7h4v-4h2v4h4V8h2z"/></svg>
        <span>Street, Building, Zip Code<br>City, Country</span>
      </li>
      <li class="contact__item">
        <svg class="contact__icon" viewBox="0 0 16 16"><path d="M4 1 1.5 3C1 8 8 15 13 14.5l2-2.5-3-3-2 1.5C8.5 9.5 6.5 7.5 5.5 6L7 4z"/></svg>
        <span>(000)0 000-0000</span>
      </li>
      <li class="contact__item">
        <svg class="contact__icon" viewBox="0 0 16 16"><path d="M4 0h8v16H4zM5.2 2v11h5.6V2z"/></svg>
        <span>(000)00 000-0000</span>
      </li>
      <li class="contact__item">
        <svg class="contact__icon" viewBox="0 0 16 16"><path d="M1 4h14v9H1zM1 4l7 5 7-5" stroke="#5e5f61" stroke-width="1"/></svg>
        <span>email@website.com</span>
      </li>
      <li class="contact__item">
        <svg class="contact__icon" viewBox="0 0 16 16"><circle cx="8" cy="8" r="7"/><path d="M1 8h14M8 1v14M3 4h10M3 12h10" stroke="#5e5f61" stroke-width="1" fill="none"/></svg>
        <span>www.website.com</span>
      </li>
    </ul>
  </section>
</main>
</body>
</html>
```